We need a need two-page flyer that talks about the services of Harbor Linkage. We like this created in ppt if possible (let me know if not). We have created the HL ppt for your reference. Please use the attached Oldharbor .pdf for reference. We like this to be fun and creative in flair and style. Something that the sales people can use and will wow the client if we email it to them.

```html
<!DOCTYPE html>
<html lang="en">
<head>
<meta charset="utf-8">
<title>Harbor Linkage – Two-Page Services Flyer</title>
<link href="https://fonts.googleapis.com/css2?family=Bebas+Neue&family=Source+Sans+3:wght@400;600;700&display=swap" rel="stylesheet">
<style>
  :root {
    --stage: #454345;
    --green: #4cae3f;
    --blue: #2e3f9e;
    --red: #e2231f;
    --ink: #222222;
    --logo-ink: #3a3a3a;
    --white: #ffffff;
  }
  * { box-sizing: border-box; margin: 0; padding: 0; }
  html, body { width: 1200px; height: 1200px; overflow: hidden; }
  body {
    background: var(--stage);
    font-family: "Source Sans 3", sans-serif;
    color: var(--ink);
    position: relative;
  }
  .page {
    position: absolute;
    width: 628px;
    height: 882px;
    background: var(--white);
    overflow: hidden;
    transform: scale(0.8);
    transform-origin: top left;
  }
  .page--services { left: 78px; top: 274px; }
  .page--approach { left: 633px; top: 274px; }
  .page-art { position: absolute; inset: 0; width: 628px; height: 882px; }
  .abs { position: absolute; }

  .brand-name {
    font-family: "Source Sans 3", sans-serif;
    font-weight: 400;
    font-size: 26px;
    letter-spacing: 1px;
    color: var(--logo-ink);
    text-transform: uppercase;
    line-height: 1;
    display: flex;
    align-items: center;
    gap: 10px;
    white-space: nowrap;
  }
  .brand-dot { width: 16px; height: 16px; border-radius: 50%; background: var(--blue); }

  .headline {
    font-family: "Bebas Neue", sans-serif;
    font-weight: 400;
    font-size: 41px;
    line-height: 38px;
    text-transform: uppercase;
    white-space: nowrap;
  }
  .headline .green { color: var(--green); display: block; }
  .headline .red { color: var(--red); display: block; }

  .strapline { font-weight: 700; font-size: 11.5px; line-height: 15px; text-transform: uppercase; }

  .pill {
    position: absolute;
    height: 23px;
    padding: 0 10px;
    border-radius: 12px;
    color: var(--white);
    font-weight: 600;
    font-size: 14px;
    line-height: 23px;
    white-space: nowrap;
  }
  .pill--red { background: var(--red); }
  .pill--blue { background: var(--blue); }

  .copy { font-size: 10.6px; line-height: 13.6px; }
  .copy p + p { margin-top: 13px; }
  .copy--light { color: var(--white); }
  .copy--right { text-align: right; }

  .check-list { list-style: none; }
  .check-list li {
    position: relative;
    padding-right: 18px;
    text-align: right;
    color: var(--white);
    font-size: 10.6px;
    line-height: 13.6px;
    height: 32px;
  }
  .check-list svg { position: absolute; right: 0; top: 4px; width: 10px; height: 9px; }

  .bullet-list { list-style: none; }
  .bullet-list li { position: relative; padding-left: 13px; font-size: 10.6px; line-height: 13.6px; margin-bottom: 6px; }
  .bullet-list li::before {
    content: "";
    position: absolute; left: 0; top: 3px;
    width: 7px; height: 7px;
    border: 1.5px solid var(--red);
    border-radius: 50%;
  }

  .contact { color: var(--white); text-align: right; font-weight: 600; font-size: 12px; line-height: 15px; }
  .contact .contact-name { font-size: 18px; line-height: 24px; font-weight: 600; }
</style>
</head>
<body>

<!-- PAGE ONE: SERVICES -->
<section class="page page--services">
  <svg class="page-art" viewBox="0 0 628 882">
    <defs>
      <linearGradient id="hangarTone" x1="0" y1="0" x2="0" y2="1">
        <stop offset="0" stop-color="#0d0d12"/>
        <stop offset="0.35" stop-color="#4a3a2c"/>
        <stop offset="0.6" stop-color="#6c6e78"/>
        <stop offset="0.78" stop-color="#0b0b0b"/>
        <stop offset="1" stop-color="#000"/>
      </linearGradient>
      <radialGradient id="shipDeckTone" cx="0.5" cy="0.5" r="0.6">
        <stop offset="0" stop-color="#3f7f95"/>
        <stop offset="1" stop-color="#123a52"/>
      </radialGradient>
    </defs>
    <!-- green band -->
    <path d="M0,225 C70,265 140,300 210,320 L628,420 L628,552 C430,540 210,555 0,600 Z" fill="var(--green)"/>
    <!-- blue sweep under green -->
    <path d="M0,600 C210,555 430,540 628,552 L628,566 C430,554 210,566 0,612 Z" fill="var(--blue)"/>
    <!-- blue arc behind photo -->
    <path d="M294,0 L628,0 L628,410 L175,330 C262,262 300,140 294,0 Z" fill="var(--blue)"/>
    <!-- red band under photo -->
    <path d="M180,352 C330,385 480,400 628,402 L628,420 C470,418 320,400 180,362 Z" fill="var(--red)"/>
    <!-- top photo -->
    <path d="M320,0 L628,0 L628,402 C470,398 320,380 192,340 C282,262 326,140 320,0 Z" fill="url(#hangarTone)" role="img" aria-label="Photo: banquet tables set inside an aircraft hangar with vintage planes overhead"/>
    <!-- left circle photo -->
    <circle cx="99" cy="302" r="94" fill="var(--red)"/>
    <circle cx="99" cy="302" r="88" fill="var(--white)"/>
    <circle cx="99" cy="302" r="82" fill="url(#shipDeckTone)" role="img" aria-label="Photo: themed ship-deck set with a wooden steering wheel under blue lighting"/>
    <!-- bottom blue band -->
    <path d="M0,808 C160,780 300,765 628,778 L628,882 L0,882 Z" fill="var(--blue)"/>
    <path d="M0,800 C160,772 300,757 628,770 L628,778 C300,765 160,780 0,808 Z" fill="var(--red)"/>
  </svg>

  <div class="abs brand-name" style="left:32px; top:38px;"><span class="brand-dot"></span>Harbor Linkage</div>

  <h1 class="abs headline" style="left:22px; top:94px;">
    <span class="green">Event Management</span>
    <span class="red">Services</span>
  </h1>
  <p class="abs strapline" style="left:22px; top:170px;">Bringing people, businesses, markets<br>and ideas together</p>

  <p class="abs copy copy--light copy--right" style="right:22px; top:305px; width:370px; font-size:11.2px; line-height:14.8px;">
    Founded in 1999, Harbor Linkage is a specialist organizer of business-to-business events, including conferences, award ceremonies, seminars, workshops, roadshows, roundtables and exhibitions for the public, commercial and third sectors.
  </p>

  <span class="pill pill--red" style="left:22px; top:417px;">Themed Props and Décor</span>
  <div class="abs copy copy--light" style="left:28px; top:451px; width:575px;">
    <p>At Harbor Linkage we are known for providing décor that completely changes the surrounds of your venue and provides your guests with an immersive event experience. Our expert event designers understand how the product will be used and where it will be most impactful.</p>
    <p>Whether being transported to outer space or to a tropical paradise, our props drive each theme home. We also will use foliage, lighting, ice, and even custom décor items</p>
  </div>

  <span class="pill pill--blue" style="left:62px; top:590px;">LED Linkage</span>
  <span class="pill pill--red" style="left:248px; top:589px;">Foliage Linkage</span>
  <span class="pill pill--blue" style="left:455px; top:591px;">Carving Ice</span>

  <div class="abs copy" style="left:18px; top:620px; width:200px;">
    <p>LED Linkage was born from the need to eliminate pesky cords at our events. Our lighted décor is now completely battery operated. We now sell most of our lights to multiple companies and theme parks throughout the United States.</p>
    <p>Our lighted products are brand friendly, meaning we can add a logo or monogram to just about any of our lighted décor items.</p>
  </div>
  <div class="abs copy" style="left:227px; top:620px; width:194px;">
    <p>Foliage Linkage is our only company that is not located on property. We have 40,000 square feet of green houses with a large selection of inventory from 14’ Amstel Ficus Trees, 12’ Palms, to lush Boston Ferns and many more in between.</p>
  </div>
  <div class="abs copy" style="left:433px; top:621px; width:178px;">
    <p>Ice sculptures are a central point and unique statement at a corporate event or wedding. Ice will attract attention and provide a memorable focal and visual for attendee discussion. It can even be an interactive experience when your guests use an ice luge for the first time or drink from a glass with a large ice cube featuring your logo!</p>
  </div>

  <span class="pill pill--red" style="left:326px; top:786px;">Custom Fabrication for All Types of Events</span>
  <p class="abs copy copy--light copy--right" style="right:19px; top:815px; width:595px;">
    At Harbor Linkage our in-house fabrication team has the ability to deliver custom designs and fabrications that will make your next event a unique one. Our team of professionals specializes in providing creative event solutions for companies planning both in-office and off-site activities. Our services provide the very best in custom staging, furniture and décor, scenic displays, tradeshow booths, and much more.
  </p>
</section>

<!-- PAGE TWO: APPROACH -->
<section class="page page--approach">
  <svg class="page-art" viewBox="0 0 628 882">
    <defs>
      <linearGradient id="stageTone" x1="0" y1="0" x2="0" y2="1">
        <stop offset="0" stop-color="#c53ee0"/>
        <stop offset="0.4" stop-color="#e7a0f2"/>
        <stop offset="0.55" stop-color="#6a1a80"/>
        <stop offset="1" stop-color="#b13ad6"/>
      </linearGradient>
      <radialGradient id="gardenTone" cx="0.5" cy="0.5" r="0.6">
        <stop offset="0" stop-color="#8a8f7a"/>
        <stop offset="1" stop-color="#4c7a3a"/>
      </radialGradient>
      <radialGradient id="jungleTone" cx="0.5" cy="0.5" r="0.6">
        <stop offset="0" stop-color="#6a6a48"/>
        <stop offset="1" stop-color="#2f6b2a"/>
      </radialGradient>
    </defs>
    <!-- green band -->
    <path d="M0,390 L628,340 L628,575 C420,580 200,586 0,592 Z" fill="var(--green)"/>
    <!-- blue sweep at green base -->
    <path d="M0,592 C200,586 420,580 628,575 L628,660 C560,622 470,604 0,604 Z" fill="var(--blue)"/>
    <!-- blue arc -->
    <path d="M0,0 L314,0 C302,130 342,215 470,262 L628,300 L628,370 L0,402 Z" fill="var(--blue)"/>
    <!-- red band -->
    <path d="M0,396 C200,395 430,370 628,338 L628,352 C430,384 200,409 0,410 Z" fill="var(--red)"/>
    <!-- stage photo -->
    <path d="M0,0 L290,0 C278,140 318,232 450,282 L628,326 L628,338 C430,370 200,395 0,396 Z" fill="url(#stageTone)" role="img" aria-label="Photo: ballroom stage and illuminated dance floor washed in magenta light"/>
    <!-- garden circle -->
    <circle cx="529" cy="281" r="92" fill="var(--red)"/>
    <circle cx="529" cy="281" r="86" fill="var(--white)"/>
    <circle cx="529" cy="281" r="80" fill="url(#gardenTone)" role="img" aria-label="Photo: outdoor garden party with palm trees, lanterns and white chairs"/>
    <!-- bottom blue band -->
    <path d="M0,800 C160,770 340,752 628,766 L628,882 L0,882 Z" fill="var(--blue)"/>
    <path d="M0,792 C160,762 340,744 628,758 L628,766 C340,752 160,770 0,800 Z" fill="var(--red)"/>
    <!-- column divider -->
    <line x1="321" y1="615" x2="321" y2="766" stroke="var(--ink)" stroke-width="1"/>
    <!-- tropical circle -->
    <circle cx="88" cy="812" r="60" fill="var(--red)"/>
    <circle cx="88" cy="812" r="55" fill="var(--white)"/>
    <circle cx="88" cy="812" r="50" fill="url(#jungleTone)" role="img" aria-label="Photo: tropical décor with palm fronds and a carved tiki prop"/>
  </svg>

  <div class="abs brand-name" style="right:40px; top:32px;"><span class="brand-dot"></span>Harbor Linkage</div>

  <h1 class="abs headline" style="right:20px; top:96px; text-align:right;">
    <span class="red">Our Approach To</span>
    <span class="green">A Successful Event</span>
  </h1>

  <span class="pill pill--blue" style="right:22px; top:411px;">An Extension of Your Own team</span>
  <ul class="abs check-list" style="right:14px; top:452px; width:600px;">
    <li>When you employ Harbor Linkage to create or manage one of your events, you can be assured that you are in the safe hands of thoroughbred event organizers.<svg viewBox="0 0 10 9"><path d="M1,5 L4,8 L9,1" fill="none" stroke="var(--blue)" stroke-width="1.8"/></svg></li>
    <li>We like to work as an extension of your own company, treating your events and brands as respectfully as we do our own and consulting carefully on all significant decisions.<svg viewBox="0 0 10 9"><path d="M1,5 L4,8 L9,1" fill="none" stroke="var(--blue)" stroke-width="1.8"/></svg></li>
    <li>We have a strong understanding of budget constraints, constantly monitoring expenditure commitments and managing the various risks involved.<svg viewBox="0 0 10 9"><path d="M1,5 L4,8 L9,1" fill="none" stroke="var(--blue)" stroke-width="1.8"/></svg></li>
    <li>We have a strong understanding of budget constraints, constantly monitoring expenditure commitments and managing the various risks involved.<svg viewBox="0 0 10 9"><path d="M1,5 L4,8 L9,1" fill="none" stroke="var(--blue)" stroke-width="1.8"/></svg></li>
  </ul>

  <span class="pill pill--red" style="left:74px; top:624px;">Budget Transparency</span>
  <ul class="abs bullet-list" style="left:22px; top:653px; width:292px;">
    <li>We always work to a pre-agreed budget and a pre-agreed management fee, based on the amount of sales, marketing and logistical time needed to manage your event.</li>
    <li>Your final bill will not differ from this pre-agreed amount unless there have been significant changes to the project along the way.</li>
  </ul>

  <span class="pill pill--red" style="left:371px; top:623px; padding:0 28px;">Meet the Team</span>
  <ul class="abs bullet-list" style="left:328px; top:654px; width:276px;">
    <li>Organizing professional events requires a significant amount of time and ‘attention-to-detail’ across a whole range of different disciplines – but we endeavor to provide a single point of contact to streamline client communications wherever possible.</li>
  </ul>

  <div class="abs contact" style="right:38px; top:793px;">
    <div class="contact-name">Harbor Linkage</div>
    <div>4120 Lantern Bay Road, Coral Haven, FL 32000</div>
    <div>(555) 014-2730 &nbsp;|&nbsp; info@harborlinkage.example</div>
    <div>www.harborlinkage.example</div>
  </div>
</section>

</body>
</html>
```